Brochure Projecct

I need a brochure created for my company, which will be sent to customers via email in PDF format. I have uploaded the company logo with this project, which I want incorporated in the design.

Designers should view the company website at www.brightcounselpages.com. I want the brochure to compliment the website (i.e., very clean design). I would also like pictures added to the brochure to make the design visually stunning.

In terms of content, I need four pages in the brochure to add four separate sections of content (one section per page). The four sections of content will be as follows (1) Search Engine Optimization Benefits (2) Increased Client Retention (3) Showcase Your Law Firm (4) Maximize Your Online ROI (5) Pricing Plans. I will give the content to the winning designer to add to the project. Each individual content section will have four subsection titles after which content of approximately 100 to 200 words will appear.

Designers can decide if other pages should be added to the brochure (i.e., a "cover page" that would have little content, but be visually appealing like the cover of a book - - - a "back page" that may just have the logo, contact information, etc).

My company address and email address should be prominently featured through every page (address: 2715 West Juniper Avenue, Suite 1400, Scottsdale, Arizona 85317; email: sales@brightcounselpages.com).

Industry/Entity Type

It Company

Requirements
Must have
• Clean look but visually stunning incorporating the design of the website at brightcounselpages.com as well as the logo. Also, room for content as set forth in the description of this project.

```html
<!DOCTYPE html>
<html lang="en">
<head>
<meta charset="utf-8">
<title>Bright Counsel Pages – Brochure Cover</title>
<link rel="stylesheet" href="https://fonts.googleapis.com/css2?family=Bowlby+One+SC&family=Arimo:wght@400;700&display=swap">
<style>
  :root {
    --blue-light: #52a9c8;
    --blue-mid: #3d86a6;
    --blue-dark: #2c5f78;
    --teal-line: #3e8ca0;
    --green: #8cb83b;
    --navy: #1e5a7a;
    --grey-light: #f6f6f6;
    --grey-mid: #e2e2e2;
    --white: #ffffff;
    --ink: #2a2a2a;
  }
  * { margin: 0; padding: 0; box-sizing: border-box; }
  html, body { width: 848px; height: 1200px; overflow: hidden; background: var(--white); }
  .cover {
    position: relative;
    width: 848px;
    height: 1200px;
    overflow: hidden;
    font-family: "Arimo", Arial, sans-serif;
    background: radial-gradient(ellipse 620px 260px at 500px 1050px, var(--grey-light) 0%, var(--grey-mid) 100%);
  }
  .cover__hero {
    position: absolute;
    left: 0; top: 0;
    width: 848px; height: 852px;
    background: radial-gradient(ellipse 520px 520px at 427px 413px, var(--blue-light) 0%, var(--blue-mid) 45%, var(--blue-dark) 100%);
  }
  .cover__band {
    position: absolute;
    left: 0; top: 852px;
    width: 848px; height: 30px;
    background: var(--white);
    border-top: 2px solid var(--teal-line);
  }
  .cover__title {
    position: absolute;
    left: 50px; top: 478px;
    font-family: "Bowlby One SC", Impact, sans-serif;
    font-size: 50px;
    line-height: 1;
    color: var(--white);
    letter-spacing: 1px;
    white-space: nowrap;
  }
  .cover__photo {
    position: absolute;
    left: 47px; top: 712px;
    width: 264px; height: 240px;
    border-radius: 14px 14px 56px 14px;
    background: linear-gradient(135deg, #4a5560 0%, #2b2f36 55%, #15181c 100%);
    overflow: hidden;
  }
  .cover__tag {
    position: absolute;
    left: 47px;
    height: 30px;
    padding: 0 10px;
    background: var(--green);
    color: var(--white);
    font-size: 16px;
    line-height: 30px;
    letter-spacing: 0.5px;
  }
  .cover__tag--first { top: 812px; width: 86px; }
  .cover__tag--second { top: 851px; width: 167px; }
  .contact {
    position: absolute;
    left: 50px; top: 1015px;
    font-size: 17px;
    font-weight: 700;
    line-height: 25px;
    color: var(--green);
  }
  .contact__label { color: var(--navy); }
  .brand {
    position: absolute;
    left: 618px; top: 1040px;
    display: flex;
    align-items: center;
    gap: 10px;
  }
  .brand__dot {
    width: 34px; height: 34px;
    border-radius: 50%;
    background: var(--blue-mid);
    flex: none;
  }
  .brand__name {
    font-family: "Arimo", Arial, sans-serif;
    font-weight: 700;
    font-size: 20px;
    line-height: 24px;
    color: var(--ink);
    width: 130px;
  }
</style>
</head>
<body>
  <main class="cover">
    <div class="cover__hero"></div>
    <div class="cover__band"></div>

    <h1 class="cover__title">BRIGHT COUNSEL PAGES</h1>

    <div class="cover__photo" role="img" aria-label="Photo of two lawyers in suits in conversation"></div>
    <div class="cover__tag cover__tag--first">SSDS</div>
    <div class="cover__tag cover__tag--second">XZCZXCXZC</div>

    <address class="contact" style="font-style: normal;">
      <div><span class="contact__label">Address:</span> 2715 West Juniper Avenue, Suite 1400,</div>
      <div>Scottsdale, Arizona 85317</div>
      <div><span class="contact__label">Email:</span> sales@brightcounselpages.com</div>
    </address>

    <div class="brand">
      <span class="brand__dot"></span>
      <span class="brand__name">Bright Counsel Pages</span>
    </div>
  </main>
</body>
</html>
```